Visitenkarten-Design für Eventcatering & Gemeinschaftsverpflegung
Zielgruppe
Wir sind ein kreatives und aufstrebendes Unternehmen.
Seit jahren sind wir im Eventcatering und der Gemeinschaftsverpflegung tätig.
Als Marktführer kochen wir super leckeres Mittagessen für Grundschulen und Kindertagesstätten in Berlin und Brandenburg und bewirtschaften mehrere Betriebsrestaurants.
Wir sind sehr krativ und bleiben nie stehen, so bereichern wir die Gastronomie in allen
Bereichen mit immer neuen innovativen Ideen und der Leidenschaft zum gesunden und leckeren Essen.
We are a creative and ambitious company.
We have been active in event catering and community catering for years.
As the market leader, we cook delicious lunches for elementary schools and day-care centers in Berlin and Brandenburg and we run several company restaurants.
We are very creative and never stand still, this is how we enrich the gastronomy in all of them
areas with new, innovative ideas and a passion for healthy and delicious food.
Aufgabenstellung
Wir möchten gern die Rottöne aus unserem Logo wiederfinden.
Unser Logo darf im Vordergrund stehen.
We would like to find the red tones from our logo again.
Our logo can be in the foreground.

```html
<!DOCTYPE html>
<html lang="de">
<head>
<meta charset="utf-8">
<title>Velora Catering – Visitenkarte</title>
<link href="https://fonts.googleapis.com/css2?family=Poppins:wght@400;600;800&display=swap" rel="stylesheet">
<style>
  :root{
    --red:#c8232b;
    --red-deep:#a81b22;
    --red-soft:#d9474d;
    --white:#ffffff;
    --ink:#1c1c1c;
    --grey:#5a5a5a;
    --stage:#ecebe9;
  }
  *{box-sizing:border-box;margin:0;padding:0}
  html,body{width:1200px;height:800px;overflow:hidden}
  body{background:var(--stage);font-family:'Poppins',sans-serif;position:relative}

  .card{position:absolute;top:230px;width:540px;height:340px;background:var(--white);
        overflow:hidden;box-shadow:0 10px 30px rgba(0,0,0,.18)}
  .card--front{left:45px}
  .card--back{left:615px}

  /* front */
  .front-band{position:absolute;left:0;top:100px;width:540px;height:125px;
        background:linear-gradient(100deg,var(--red-deep),var(--red) 45%,var(--red-soft));
        clip-path:polygon(70px 0,540px 0,540px 100%,0 100%)}
  .person{position:absolute;left:30px;top:30px}
  .person__name{color:var(--red);font-weight:800;font-size:23px;line-height:1.1}
  .person__role{color:var(--grey);font-weight:400;font-size:13px;margin-top:2px}

  .brand{position:absolute;display:flex;align-items:center;gap:8px;color:var(--ink);
        font-weight:600;white-space:nowrap}
  .brand__mark{background:var(--red);border-radius:3px;flex:none}
  .front .brand{right:28px;top:34px;font-size:17px}
  .front .brand__mark{width:22px;height:22px}

  .services{position:absolute;left:150px;top:140px;width:370px;color:var(--white);
        font-weight:600;font-size:13px;line-height:1.6;text-align:center}

  .contacts{position:absolute;left:24px;right:24px;top:268px;display:flex;justify-content:space-between;
        font-weight:600;font-size:10.5px;color:var(--ink);white-space:nowrap}
  .contact{display:flex;align-items:center;gap:6px}
  .contact svg{width:16px;height:16px;flex:none}

  /* back */
  .back-photo{position:absolute;left:0;top:0;width:540px;height:210px;
        background:radial-gradient(ellipse at 30% 45%,#b9673a 0,#c98a55 18%,#e6e2dc 40%),
                   radial-gradient(ellipse at 78% 55%,#b5663a 0,#e6e2dc 35%);
        background-blend-mode:multiply}
  .back-shapes{position:absolute;inset:0}
  .back .brand{right:34px;bottom:74px;font-size:24px}
  .back .brand__mark{width:30px;height:30px}
</style>
</head>
<body>

<section class="card card--front front">
  <div class="front-band" role="img" aria-label="Rotes Band mit blasser Aufnahme von Speisen"></div>

  <div class="person">
    <p class="person__name">Jonas Beispiel</p>
    <p class="person__role">Director</p>
  </div>

  <div class="brand"><span class="brand__mark"></span>Velora Catering</div>

  <p class="services">Oberschulen - Grundschulen - Kindergarten<br>Betriebsgastronomie - Tagungsraum</p>

  <div class="contacts">
    <span class="contact">
      <svg viewBox="0 0 20 20"><path d="M2 5h16v11H2z" fill="#c8232b"/><path d="M2 5l8 6 8-6" fill="none" stroke="#fff" stroke-width="1.5"/></svg>
      info@velora-catering.de
    </span>
    <span class="contact">
      <svg viewBox="0 0 20 20"><path d="M5 2l3 4-2 2c1 2 3 4 5 5l2-2 4 3-2 4C8 17 3 12 2 5z" fill="#c8232b"/></svg>
      030 | 512 887 40
    </span>
    <span class="contact">
      <svg viewBox="0 0 20 20" fill="none" stroke="#c8232b" stroke-width="1.6"><circle cx="10" cy="10" r="8"/><ellipse cx="10" cy="10" rx="3.5" ry="8"/><path d="M2 10h16M4 5.5h12M4 14.5h12"/></svg>
      www.velora-catering.de
    </span>
  </div>
</section>

<section class="card card--back back">
  <div class="back-photo" role="img" aria-label="Foto von Schalen mit Ofenkartoffeln, Salat und Dip auf hellem Tisch"></div>
  <svg class="back-shapes" viewBox="0 0 540 340" aria-hidden="true">
    <path d="M0 150 C140 140 300 150 540 200 L540 340 L0 340 Z" fill="#c8232b"/>
    <path d="M80 340 C160 240 300 190 460 180 Q525 176 525 235 L525 275 C440 295 360 315 290 340 Z" fill="#ffffff"/>
  </svg>
  <div class="brand"><span class="brand__mark"></span>Velora Catering</div>
</section>

</body>
</html>
```